LeaseWiser - Apartment Reviews Website Concept Sketch

IMPORTANT UPDATES BELOW -

Current Contest:
Deliverable: 1 or more original design concepts for website home-page. A guaranteed payment will be made to the lead design.

Context:
This guaranteed-payment contest is for submission of 1 or more concept sketches for the home page of the website described below.

Based on finalist submissions, a freelance contract may be let for design-only development (PSDs only) of the full site, approximately 20 pages. Budget for the full site design is $3000 - $5000 and will include multiple rounds to refine the home-page concept and then to extend the design to the full site.

All mySql and PHP logic is already coded and working. No coding is required for the contest or the follow-on project.

IMPORTANT UPDATES ABOVE -

The Website:

LeaseWiser is developing an on-line, searchable, pay-for-access database of user-contributed reviews of apartment complexes. Consumers will use these reviews to make better informed decisions before committing to an apartment lease.

We currently have a functional, wireframe-only website accessible at leasewiser.example. The wireframes are under development, and site pages may display debugging information or may be inaccessible on occasion.

Additional information as well as a site map is available at: leasewiser.example/qqstudio.

We require complete graphic design for a multi-page, interactive, database-driven website. Cutting and coding the design into the existing php code base is a separate project, but feel free to quote on this separately if you have capabilities. We do not require any software or database development. All software is proprietary, we are not using any third-party platform for CMS, survey management, etc.

Attributes we wish to convey with our logo, website, and other presentation:
• Trustworthiness – users should expect the information we present to be accurate and complete
• Impartiality - users can rely on the survey results we present not to be influenced or “bought” by apartment managers
• Professionalism – LeaseWiser is a team of professionals dedicated to building and delivering a high-value, high-relevance database of fresh information that will help apartment renters make better decisions about where to live. We are not an informal community, not a group of volunteers, and not a free-access, open source product.
• Simplicity – our site is easy to use, easy to search, and our survey results are easy to understand
• Accessibility – anyone can use our service, it is not just for experts or people with technical skills
• Affordability – our service is priced at a point (about $50 for 90-days use) that it is affordable for everyone who plans to rent an apartment and makes economic sense as insurance against making an uninformed decision (much less than the cost of a month’s rent)
• Interest to Apartment Dwellers – our name, and preferably our logo, identifies us immediately as being of interest to apartment renters and seekers
• Positive Outlook – although the greatest value of LeaseWiser will be in helping apartment hunters avoid buildings with construction, management, and neighborhood problems, our website imagery should not focus on the negative aspects, but rather on the happiness, security, and satisfaction that comes with a good selection of an apartment

Website Purpose
During Phase 1 (current) of LeaseWiser’s development, the purpose of the website is to collect apartment reviews. Traffic will be driven by a display/performance ad campaign. We are assembling a business asset (the database) and this is really a direct response marketing campaign. We will offer a variety of incentives (sweepstakes entries, gift card redemption) to induce people to complete a survey and view a series of advertising offers. During Phase 1, there will be no database of apartment reviews for users to preview, and nothing for us to sell.

During Phase 2 (future) of LeaseWiser’s development, the purpose of the website will be to induce members to pay to access the database, and to provide a means for paying customers to access the database of reviews. Phase 2 is NOT in scope at this time, but will represent a substantial future upgrade - naturally the original design team will be in a strong competitive position for this future work.

The LeaseWiser website has a small area that will serve our advertising partners so they can access campaign and reporting information. This part of the site will need a simple but professional design treatment and is within the scope of Phase 1 development.

Our primary creative goal at this time is to present a website that supports Phase 1 goals. Many of the pages necessary for Phase 2 operation are outside the scope of the Phase 1 creative effort, in particular previewing reviews, searching the database, viewing search results, and transaction-oriented pages.
Updates

Project Deadline Extended
Reason: We didn't communicate the nature of the Design Contest well. We are extending the deadline to permit designers to re-evaluate the scope of the current work in the context of the award amount.

Target Market(s)

Our market audience is internet-savvy Americans who live in or are moving into an apartment.

Industry/Entity Type

Graphic Design

Requirements
Must have
• We are finalizing logo design and have posted a draft copy on the site. Logo design is still subject to refinement, but the basic concept is frozen. Colors / combinations may change, but will be arena of blue or blue+green.

Key elements of the home page are:
- a call to action to review an apartment
- room for 1-2 rotating articles about selecting an apartment, planning a move, shopping for insurance in your new location, etc. to act as light-weight, added value elements for site visitors.

Important to know:
- The survey itself (reviewapartment.php - only accessible by following all the steps starting with the "review an apartment" link) is database-driven, so the design must be able to accommodate assembly of questions in different formats using a building-block approach. The current wire-frame illustrates the major question/answer formats: radio; checkbox; matrix-radio; free-text.

Over the life of the project, we will undoubtedly build dozens of landing pages that center around the call to action of "review the apartment where you live" with various inducements (sweepstakes entry, redeemable incentives, social appeals, etc.) Development of these landing pages is a separate project, but the initial design should include one or two. If direct-marketing design / landing page design is not your forte, these pages can be removed from the scope of the web design project.

Should not have
• We would prefer to stay away from flash-heavy pages for the website.

```html
<!DOCTYPE html>
<html lang="en">
<head>
<meta charset="utf-8">
<title>LeaseWiser – Home</title>
<link rel="stylesheet" href="https://fonts.googleapis.com/css2?family=Lato:wght@400;700;900&display=swap">
<style>
:root{
  --blue:#005cbe;
  --blue-dark:#0a4fa0;
  --green:#7ab800;
  --green-light:#a6d93a;
  --yellow:#f7d117;
  --winner-yellow:#f4f000;
  --caption-green:#d8f78e;
  --ink:#111;
  --white:#fff;
}
*{box-sizing:border-box;margin:0;padding:0}
html,body{width:1200px;height:981px;overflow:hidden;background:var(--white);font-family:"Lato",sans-serif;color:var(--ink)}
.page{position:relative;width:1200px;height:981px}

/* top bar */
.topbar{position:absolute;left:0;top:0;width:1200px;height:50px;background:var(--blue)}
.topbar-stripe{position:absolute;left:0;top:50px;width:1200px;height:6px;background:var(--green);box-shadow:0 2px 4px rgba(0,0,0,.3)}
.share{position:absolute;top:16px;display:flex;align-items:center;gap:4px;font-size:11px;white-space:nowrap}
.share-btn{height:19px;padding:0 6px;border-radius:3px;background:#eef1f6;border:1px solid #c6ccd8;color:#333;font-weight:700;display:flex;align-items:center;gap:4px}
.share-btn .dot{width:10px;height:10px;background:#8a98b0}
.share-btn.alt{background:#e9573b;border-color:#d1452b;color:var(--white)}
.share-btn.alt .dot{background:var(--white)}
.share-count{height:19px;padding:0 4px;background:var(--white);border:1px solid #c6ccd8;color:#333;display:flex;align-items:center;border-radius:2px}
.utility{position:absolute;top:15px;right:123px;display:flex;align-items:center;color:var(--white);font-size:17px;font-weight:700;white-space:nowrap}
.utility a{display:flex;align-items:center;gap:4px;padding:0 14px;border-left:1px solid rgba(255,255,255,.35);color:inherit;text-decoration:none}
.utility a:first-child{border-left:none}
.utility a:last-child{padding-right:0}

/* brand */
.brand{position:absolute;left:130px;top:100px;display:flex;align-items:center;gap:10px}
.brand-mark{width:30px;height:30px;background:var(--green)}
.brand-name{font-size:42px;font-weight:900;color:var(--green);letter-spacing:-1px}

/* nav */
.mainnav{position:absolute;left:103px;top:187px;width:1000px;height:56px;background:var(--blue)}
.mainnav-stripe{position:absolute;left:103px;top:243px;width:1000px;height:7px;background:var(--green)}
.mainnav ul{list-style:none;position:absolute;right:8px;top:6px;display:flex;height:50px;white-space:nowrap}
.mainnav li{font-size:21px;font-weight:700;color:var(--white);text-transform:uppercase;padding:10px 15px 0;letter-spacing:.3px}
.mainnav li.active{background:var(--green);border:1px solid #c8e890;border-bottom:none;border-radius:4px 4px 0 0;padding:9px 10px 0;margin-right:18px}

/* hero */
.hero{position:absolute;left:103px;top:250px;width:1000px;height:295px;overflow:hidden}
.hero-photo{position:absolute;inset:0;background:linear-gradient(100deg,#e7e8e6 0%,#cfd2d0 35%,#b9a89a 60%,#8c7668 80%,#d9dcd8 100%)}
.hero-headline{position:absolute;left:0;top:51px;width:538px;height:64px;background:rgba(0,92,190,.82);color:var(--white);font-size:34px;font-weight:900;padding:11px 0 0 30px;letter-spacing:.3px;white-space:nowrap}
.hero-cta{position:absolute;left:194px;top:145px;width:200px;height:60px;border-radius:8px;background:linear-gradient(#ffe35a,#f7b700);box-shadow:2px 3px 4px rgba(0,0,0,.3);padding:9px 0 0 20px;white-space:nowrap}
.hero-cta .big{display:block;font-size:27px;font-weight:900;color:var(--blue);line-height:26px;letter-spacing:-.3px}
.hero-cta .small{display:block;font-size:15px;font-weight:700;color:var(--ink);line-height:16px;margin-left:3px}
.hero-caption{position:absolute;left:193px;top:244px;width:807px;height:31px;background:rgba(0,92,190,.8);color:var(--caption-green);font-size:21px;font-weight:700;padding:2px 0 0 36px;letter-spacing:1px;white-space:nowrap}

/* intro */
.intro{position:absolute;left:111px;top:569px;width:985px}
.intro h2{font-size:24px;font-weight:900;color:var(--blue);margin-bottom:6px}
.intro p{font-size:16.5px;font-weight:700;line-height:22px}

/* winner band */
.winner{position:absolute;left:103px;top:691px;width:1000px;height:85px;background:var(--blue);border-top:8px solid var(--yellow);border-bottom:8px solid var(--yellow)}
.winner-star{position:absolute;left:16px;top:-1px}
.winner h3{position:absolute;left:41px;top:4px;font-size:41px;font-weight:700;color:var(--winner-yellow);line-height:44px;white-space:nowrap}
.winner p{position:absolute;left:40px;top:50px;font-size:12.5px;font-weight:700;color:var(--white);white-space:nowrap}
.winner-btn{position:absolute;left:739px;top:10px;width:228px;height:44px;border-radius:5px;background:linear-gradient(#c4ec6a,#6fb400);box-shadow:2px 3px 4px rgba(0,0,0,.35);color:var(--blue-dark);font-size:30px;font-weight:700;text-align:center;line-height:43px;white-space:nowrap}

/* footer */
.footer-stripe{position:absolute;left:0;top:797px;width:1200px;height:6px;background:var(--green);box-shadow:0 -2px 4px rgba(0,0,0,.3)}
.footer{position:absolute;left:0;top:803px;width:1200px;height:178px;background:var(--blue);color:var(--white)}
.footer-links{position:absolute;left:102px;top:17px;display:flex;list-style:none;font-size:17px;font-weight:700;white-space:nowrap}
.footer-links li{padding:0 11px;border-left:1px solid rgba(255,255,255,.4);line-height:18px}
.footer-links li:first-child{padding-left:0;border-left:none}
.copyright{position:absolute;left:103px;top:133px;font-size:16px;font-weight:700;white-space:nowrap}
.footer-brand{position:absolute;left:418px;top:117px;width:74px;height:33px;background:var(--white);color:var(--green);font-size:12px;font-weight:900;display:flex;align-items:center;justify-content:center}
.social{position:absolute;left:1041px;top:107px;font-size:12px;font-weight:700;white-space:nowrap}
.social-icons{display:flex;gap:8px;margin-top:2px}
.social-icons span{width:26px;height:26px;background:#8fb6e0;border-radius:2px}
</style>
</head>
<body>
<div class="page">
  <header>
    <div class="topbar">
      <div class="share" style="left:105px"><span class="share-btn"><i class="dot"></i>Like</span><span class="share-count">2k</span></div>
      <div class="share" style="left:199px"><span class="share-btn"><i class="dot"></i>Post</span><span class="share-count">1,100</span></div>
      <div class="share" style="left:312px"><span class="share-btn">+1</span><span class="share-count">117</span></div>
      <div class="share" style="left:404px"><span class="share-btn alt"><i class="dot"></i>Share</span><span class="share-count">1.2K</span></div>
      <nav class="utility">
        <a href="#"><svg width="12" height="15" viewBox="0 0 12 15"><path d="M1 1h7l3 3v10H1z" fill="#fff"/></svg>Terms and Conditions</a>
        <a href="#"><svg width="14" height="14" viewBox="0 0 14 14"><circle cx="7" cy="7" r="6" fill="#fff"/><text x="7" y="11" font-size="10" font-weight="700" text-anchor="middle" fill="#005cbe">?</text></svg>Faq</a>
        <a href="#"><svg width="12" height="15" viewBox="0 0 12 15"><path d="M3 7V4a3 3 0 0 1 6 0v3" stroke="#fff" stroke-width="1.6" fill="none"/><rect x="1" y="7" width="10" height="7" fill="#fff"/></svg>Login</a>
      </nav>
    </div>
    <div class="topbar-stripe"></div>
    <div class="brand"><span class="brand-mark"></span><span class="brand-name">LeaseWiser</span></div>
    <nav class="mainnav">
      <ul>
        <li class="active">Home</li>
        <li>Review an Apartment</li>
        <li>Enter Sweeps</li>
        <li>Contest Rules</li>
      </ul>
    </nav>
    <div class="mainnav-stripe"></div>
  </header>

  <section class="hero">
    <div class="hero-photo" role="img" aria-label="Photo of a smiling mother and daughter in front of a white house"></div>
    <h1 class="hero-headline">WIN A HOME OF YOUR OWN!</h1>
    <a class="hero-cta"><span class="big">ENTER NOW</span><span class="small">start reviewing</span></a>
    <p class="hero-caption">Just review the apartment where you live and you'll be entered to win!*</p>
  </section>

  <section class="intro">
    <h2>SweepStakes</h2>
    <p>Lorem ipsum dolor sit amet, consectetur adipiscing elit. Pellentesque vel tortor orci. Fusce magna odio, hendrerit quis malesuada ut, blandit ut tellus. Integer in tellus urna. Aliquam quis congue dui. Curabitur posuere placerat elit id mollis. Praesent iaculis quam sed mi sodales feugiat. Pellentesque ut arcu eget lorem vestibulum bibendum nec vel arcu.</p>
  </section>

  <section class="winner">
    <svg class="winner-star" width="24" height="26" viewBox="0 0 24 26"><rect x="7" y="0" width="10" height="8" fill="#8fb6e0"/><path d="M12 4l3 7 7 .6-5.4 4.6 1.7 7L12 19.5 5.7 23.2l1.7-7L2 11.6 9 11z" fill="#f7c948" stroke="#fff" stroke-width="1"/></svg>
    <h3>Are you our next winner</h3>
    <p>Pellentesque vel tortor orci. Fusce magna odio, hendrerit quis malesuada ut, blandit ut tellus. Integer in tellus urna</p>
    <a class="winner-btn">Enter Sweeps</a>
  </section>

  <div class="footer-stripe"></div>
  <footer class="footer">
    <ul class="footer-links">
      <li>Home</li><li>My Profile</li><li>FAQ</li><li>Terms of Use</li><li>Privacy Policy</li><li>Contest Rules</li><li>About Us</li><li>Business Opportunities</li>
    </ul>
    <p class="copyright">© Copyright 2011, 2012 LeaseWiser, LLC</p>
    <div class="footer-brand">LeaseWiser</div>
    <div class="social">Join Us on<div class="social-icons"><span></span><span></span></div></div>
  </footer>
</div>
</body>
</html>
```